Lateral thinking Law Firm needs business cards that inspire trust and value

Hi team. After great success with artflockly putting together a sign for us at our local roller-skating rink (yes, we're that cool), we've decided to ask for some designs for our new business cards.

The first card is for Martin Valcourt, Principal, Valcourt Law.
The colours should be blue, white and have some black (no red). Our logo is attached. Please don't use scales of justice, gavels, Court arches, or the blind lady of justice. We find those to cliché.

We want our cards to be eye catching, but classy in line with the legal profession, and showing a depth of character and trust. We are down to earth, highly approachable and modern in approach.

We want our clients to see us as different to the usual stuck up, boring old law firms, but at the same time, to know that we're the strongest, most genuine and dependent part on their team.

Hope that gives you some ideas for our cards. We are based in the Perth Hills (Kelmarton) and our Principal (Martin) has lived in this area for over 40 years.

We love to work with our local community where we can, but do offer services right across the State.

Martin's card should include his mobile number 0417 382 907 and email address martin@valcourtlaw-example.com, plus our website www@valcourtlaw-example.com (which is not yet prepared, but hopefully will be soon!) and mailing address PO Box 817 Kelmarton, WA 6093.

The cards should also include our practice areas - Family Law, Wills and Estates, Building and Construction, Corporate and Commercial, Local Government, Dispute Resolution & Advisory

UPDATE - If designers have the capabilities, please place a QR Code on the back of the card that encodes the business card information as a V-Card.

UPDATE - Please include mailing address PO Box 817 Kelmarton, WA 6093

```html
<!DOCTYPE html>
<html lang="en">
<head>
<meta charset="utf-8">
<title>Valcourt Law – Business Card</title>
<link href="https://fonts.googleapis.com/css2?family=Noto+Serif:wght@400;700&display=swap" rel="stylesheet">
<style>
  :root {
    --brand-blue: #4a72c8;
    --card-white: #ffffff;
    --backdrop: #3b3b3b;
  }
  * { margin: 0; padding: 0; box-sizing: border-box; }
  html, body {
    width: 1200px; height: 689px; overflow: hidden;
    background: var(--backdrop);
    font-family: "Noto Serif", Georgia, serif;
  }
  .stage { position: relative; width: 1200px; height: 689px; }
  .card {
    position: absolute; top: 195px;
    width: 520px; height: 300px; border-radius: 18px;
    box-shadow: 0 14px 30px rgba(0,0,0,.45);
  }
  .card--back { left: 50px; background: var(--brand-blue); color: var(--card-white); text-align: center; }
  .card--front { left: 630px; background: var(--card-white); color: var(--brand-blue); }

  .brand {
    display: flex; align-items: center; gap: 10px;
    font-size: 26px; font-weight: 400; letter-spacing: 2px; line-height: 1;
  }
  .brand__square { width: 10px; height: 10px; background: currentColor; flex: none; }

  .card--back .brand { position: absolute; top: 74px; left: 0; right: 0; justify-content: center; }
  .practice { position: absolute; top: 150px; left: 0; right: 0; }
  .practice__heading { font-size: 20px; font-weight: 700; letter-spacing: 2px; margin-bottom: 8px; }
  .practice__list { font-size: 13px; line-height: 1.6; letter-spacing: .3px; }

  .card--front .brand { position: absolute; top: 50px; right: 40px; }
  .person { position: absolute; left: 36px; top: 132px; }
  .person__name { font-size: 22px; font-weight: 700; letter-spacing: .5px; text-transform: uppercase; }
  .person__role { font-size: 14px; margin-top: 2px; }
  .divider { position: absolute; left: 36px; right: 36px; top: 196px; height: 2px; background: var(--brand-blue); }
  .contacts { position: absolute; left: 36px; top: 210px; list-style: none; font-size: 13px; line-height: 1.75; }
  .contacts li { display: flex; align-items: center; gap: 8px; }
  .contacts svg { width: 12px; height: 12px; flex: none; }
  .address { position: absolute; right: 36px; top: 210px; text-align: right; font-size: 13px; line-height: 1.6; }
</style>
</head>
<body>
<div class="stage">
  <section class="card card--back">
    <div class="brand"><span class="brand__square"></span><span class="brand__name">Valcourt Law</span></div>
    <div class="practice">
      <h2 class="practice__heading">OUR PRACTICE AREAS</h2>
      <p class="practice__list">Family Law | Wills and Estates<br>Building and Construction | Corporate and Commercial<br>Local Government | Dispute Resolution &amp; Advisory</p>
    </div>
  </section>

  <section class="card card--front">
    <div class="brand"><span class="brand__square"></span><span class="brand__name">Valcourt Law</span></div>
    <div class="person">
      <div class="person__name">Martin Valcourt</div>
      <div class="person__role">Principal</div>
    </div>
    <div class="divider"></div>
    <ul class="contacts">
      <li><svg viewBox="0 0 12 12"><rect x="3" y="0.5" width="6" height="11" rx="1.2" fill="none" stroke="currentColor" stroke-width="1.2"/><circle cx="6" cy="9.6" r=".7" fill="currentColor"/></svg>0417 382 907</li>
      <li><svg viewBox="0 0 12 12"><rect x="0.5" y="2" width="11" height="8" fill="currentColor"/><path d="M0.5 2 L6 7 L11.5 2" fill="none" stroke="#fff" stroke-width="1"/></svg>martin@valcourtlaw-example.com</li>
      <li><svg viewBox="0 0 12 12"><circle cx="6" cy="6" r="5.2" fill="none" stroke="currentColor" stroke-width="1.2"/><path d="M1 6 H11 M6 1 C3 4 3 8 6 11 M6 1 C9 4 9 8 6 11" fill="none" stroke="currentColor" stroke-width=".9"/></svg>valcourtlaw-example.com</li>
    </ul>
    <div class="address">PO Box 817<br>Kelmarton<br>WA 6093</div>
  </section>
</div>
</body>
</html>
```